Social Media covers for a vacation rental startup

TivTiv.com is a property management company that specializes in the short-term rental of beach houses in the coast of the Arabian Gulf (aka the Persian Gulf) in Kuwait.

TivTiv.com allows users to browse through a list of beach houses and make the booking easily. The main characteristic of tivtiv is simplicity. The identity of the company is based around minimalist design with no frills.

We need a to design a facebook page. I would like to use this page for google plus and Youtube.

Check out our website on tivtiv.com
Updates

Target Market(s)

People looking for short term rental in Kuwait.

Typically young mothers or young men looking to spend time with their friends.

Industry/Entity Type

It Company

Colors
3176b5
85acd3
f68e4e

Requirements
Must have
• The pictures should reflect the Kuwaiti beach environment.
Nice to have
• There should be no mountains and no palm trees.
• The environment in Kuwait does not have these elements.

```html
<!DOCTYPE html>
<html lang="en">
<head>
<meta charset="utf-8">
<title>TivTiv – Social Page Cover</title>
<link href="https://fonts.googleapis.com/css2?family=Roboto+Condensed:ital,wght@0,400;0,700;1,400&display=swap" rel="stylesheet">
<style>
  :root {
    --page-bg: #eef1f5;
    --card-white: #ffffff;
    --brand-orange: #f07d00;
    --band-yellow: #f2b01e;
    --band-blue: #1e96d4;
    --band-sky: #14b4e8;
    --text-white: #ffffff;
    --frame-grey: #b9b9b9;
  }
  html, body {
    margin: 0;
    width: 1200px;
    height: 1000px;
    overflow: hidden;
    background: var(--page-bg);
    font-family: "Roboto Condensed", Arial, sans-serif;
  }
  .cover-design {
    position: absolute;
    left: 50px;
    top: 266px;
    width: 1100px;
    height: 468px;
    background: var(--card-white);
  }
  .cover-photo {
    position: absolute;
    inset: 0 0 auto 0;
    height: 408px;
    background:
      linear-gradient(to bottom, rgba(0,0,0,0) 70%, rgba(0,0,0,0.45) 100%),
      linear-gradient(to bottom, #8fb6c9 0%, #c9dde6 30%, #e6ebe6 55%, #d6d2c4 78%, #8d8a78 100%);
  }
  .brand-name {
    position: absolute;
    left: 26px;
    top: 40px;
    margin: 0;
    font-size: 74px;
    font-weight: 700;
    line-height: 1;
    color: var(--brand-orange);
  }
  .feature-band {
    position: absolute;
    right: 0;
    height: 69px;
    display: flex;
    align-items: center;
    justify-content: flex-end;
    gap: 20px;
    padding-right: 16px;
    box-sizing: border-box;
    color: var(--text-white);
    font-style: italic;
    font-size: 24px;
    text-transform: uppercase;
    white-space: nowrap;
  }
  .feature-band svg { width: 50px; height: 50px; flex: none; }
  .band-family { top: 56px; width: 304px; background: linear-gradient(to right, rgba(242,176,30,0), var(--band-yellow) 22%); }
  .band-chores { top: 142px; width: 479px; background: linear-gradient(to right, rgba(30,150,212,0), var(--band-blue) 12%); }
  .band-support { top: 229px; width: 337px; background: linear-gradient(to right, rgba(20,180,232,0), var(--band-sky) 20%); }
  .profile-box {
    position: absolute;
    left: 17px;
    top: 224px;
    width: 224px;
    height: 224px;
    box-sizing: border-box;
    background: var(--card-white);
    border: 2px solid var(--frame-grey);
    box-shadow: 0 1px 3px rgba(0,0,0,0.3);
    display: flex;
    align-items: center;
    justify-content: center;
    gap: 10px;
  }
  .profile-mark {
    width: 22px; height: 22px; border-radius: 50%;
    background: var(--brand-orange);
  }
  .profile-name {
    font-size: 44px;
    font-weight: 700;
    color: var(--brand-orange);
  }
  .page-title {
    position: absolute;
    left: 258px;
    top: 326px;
    font-size: 29px;
    font-weight: 700;
    color: var(--text-white);
    text-shadow: 0 1px 3px rgba(0,0,0,0.6);
  }
</style>
</head>
<body>
  <section class="cover-design">
    <div class="cover-photo" role="img" aria-label="Photo of a beach house garden with sand, trees and the sea in the background"></div>

    <h1 class="brand-name">TivTiv</h1>

    <div class="feature-band band-family">
      <span>A family home</span>
      <svg viewBox="0 0 50 50" fill="none" stroke="#fff" stroke-width="2" stroke-linecap="round" aria-hidden="true">
        <line x1="25" y1="4" x2="25" y2="14"/>
        <path d="M10 22 Q25 10 40 22"/>
        <line x1="12" y1="22" x2="12" y2="32"/><circle cx="12" cy="36" r="4"/>
        <line x1="25" y1="18" x2="25" y2="30"/><circle cx="25" cy="34" r="4"/>
        <line x1="38" y1="22" x2="38" y2="32"/><circle cx="38" cy="36" r="4"/>
      </svg>
    </div>

    <div class="feature-band band-chores">
      <span>Home chores are taken care of</span>
      <svg viewBox="0 0 50 50" fill="none" stroke="#fff" stroke-width="2" stroke-linecap="round" stroke-linejoin="round" aria-hidden="true">
        <path d="M21 10 a4 4 0 1 1 4 4 v4"/>
        <path d="M25 18 L6 30 H44 Z"/>
        <rect x="14" y="30" width="22" height="14"/>
        <line x1="18" y1="44" x2="18" y2="47"/><line x1="25" y1="44" x2="25" y2="47"/><line x1="32" y1="44" x2="32" y2="47"/>
      </svg>
    </div>

    <div class="feature-band band-support">
      <span>One support line</span>
      <svg viewBox="0 0 50 50" fill="none" stroke="#fff" stroke-width="2" stroke-linecap="round" stroke-linejoin="round" aria-hidden="true">
        <path d="M8 14 l6 -4 l6 8 l-4 4 q4 8 10 12 l4 -4 l8 6 l-4 6 q-16 -2 -26 -28 z"/>
        <text x="27" y="26" fill="#fff" stroke="none" font-size="12" font-weight="700" font-family="Roboto Condensed, Arial, sans-serif">24</text>
        <path d="M24 6 l1 4 M32 4 v4 M40 7 l-2 3 M45 14 l-4 2 M46 22 h-4" />
      </svg>
    </div>

    <div class="page-title">TivTiv</div>

    <div class="profile-box">
      <span class="profile-mark"></span>
      <span class="profile-name">TivTiv</span>
    </div>
  </section>
</body>
</html>
```